Brightfern IT Solutions Web Design

We are a new business in Perth Australia specializing in supporting Home residential and Small business with their IT requirements
We believe image and presentation is important and having a eye catching, professional, intuitive website is a must.
Although we are still expanding as business the message we would like to convey to users is that they can trust our work.

Services we provide are
Please refer to text file attached

Future services
- Email hosting
- Domain resller
- Cloud services

A wordpress theme i really like is below.
http://www.quillmarket-example.com/site-themes/58314.html
Orange colour included is a preference however a colour that goes withg my logo is fine too.

The logo i would like to include is also attached.

I would like the web site design to be built and coded in wordpress and handed over to me so i can continue updating the content, source will be require.

Target Market(s)

Home residential and Small business users

Industry/Entity Type

Residential

Requirements
Must have
• The form to email function in the contact us page.
Nice to have
• Interactive icons

```html
<!DOCTYPE html>
<html lang="en">
<head>
<meta charset="utf-8">
<title>Brightfern IT Solutions</title>
<link href="https://fonts.googleapis.com/css2?family=PT+Sans:wght@400;700&family=Oswald:wght@600;700&display=swap" rel="stylesheet">
<style>
:root{
  --orange:#f07522;
  --orange-dark:#b9490c;
  --ink:#1d1d1d;
  --text:#6b6b6b;
  --band:#f7f7f7;
  --footer:#333333;
  --footer-line:#6a6a6a;
  --white:#ffffff;
}
*{margin:0;padding:0;box-sizing:border-box}
html,body{width:717px;height:1200px;overflow:hidden;background:var(--white)}
body{position:relative;font-family:"PT Sans",Arial,sans-serif;color:var(--text)}
.abs{position:absolute}
ul{list-style:none}

/* hero */
.hero{left:0;top:0;width:717px;height:299px;
  background:radial-gradient(ellipse at 70% 45%,#e9c2a4 0%,#d8b49a 22%,#cfc7bf 45%,#bfb7ae 70%,#8d8279 100%)}
.brand{left:54px;top:16px;display:flex;align-items:center;gap:6px}
.brand-mark{width:20px;height:20px;background:var(--orange)}
.brand-name{font-weight:700;font-size:15px;color:var(--ink);letter-spacing:.3px;white-space:nowrap}
.nav-bar{left:364px;top:10px;width:353px;height:40px;background:rgba(40,40,40,.72)}
.nav-link{top:22px;font-size:8px;color:var(--white);text-decoration:none;font-weight:700;letter-spacing:.3px;white-space:nowrap}
.nav-link.active{color:var(--orange)}
.nav-underline{left:390px;top:33px;width:36px;height:1px;background:var(--orange)}
.dropdown{left:518px;top:42px;width:107px;background:#2e2e2e;border-top:2px solid var(--orange)}
.dropdown li{height:19px;line-height:19px;font-size:6.6px;color:var(--white);padding-left:9px;white-space:nowrap}
.dropdown li.on{background:var(--orange)}
.hero-text{left:0;top:152px;width:730px;text-align:center;font-weight:700;line-height:1;
  text-shadow:1px 1px 2px rgba(0,0,0,.35)}
.hero-text .lead{font-size:26px;color:var(--orange);letter-spacing:.5px}
.hero-text .sub{font-size:18px;color:var(--white);font-weight:400;margin-top:4px;letter-spacing:.5px}
.dots{left:356px;top:272px;display:flex;gap:6px}
.dots span{width:5px;height:5px;background:var(--white)}
.dots span.on{background:#333}

/* support band */
.band{left:0;top:299px;width:717px;height:58px;background:var(--band);border-bottom:1px solid #d9d9d9}
.band-text{left:62px;top:316px;font-size:13px;color:var(--orange);white-space:nowrap}
.band-text b{color:var(--ink);font-size:15px}
.band-text .big{color:var(--ink);font-weight:700;font-size:19px}
.pill{background:var(--orange);color:var(--white);border-radius:12px;text-align:center}
.connect{left:535px;top:315px;width:115px;height:23px;line-height:23px;font-size:10px;letter-spacing:.3px}

/* welcome */
.section-title{font-weight:700;color:var(--ink);font-size:12.5px;white-space:nowrap}
.section-title .accent{color:var(--orange)}
.rule{height:4px;background:repeating-linear-gradient(90deg,#d4d4d4 0 1px,transparent 1px 2px)}
.welcome-title{left:65px;top:390px}
.welcome-rule{left:310px;top:395px;width:137px}
.welcome-copy{left:62px;top:416px;width:386px;font-size:6.8px;line-height:16px}
.read-more{left:62px;top:555px;width:54px;height:16px;line-height:16px;font-size:6.5px}
.promo{left:509px;top:389px;width:163px;height:167px;
  background:linear-gradient(160deg,#ffffff 0%,#e8f4fb 40%,#b8dcef 100%);border:1px solid #e0e0e0;text-align:center}
.promo p{font-size:7px;font-weight:700;color:var(--ink);margin-top:12px}
.promo h3{font-size:14px;color:#e1142a;font-weight:700;line-height:1.1}
.promo small{font-size:7px;color:var(--ink)}
.promo-art{left:529px;top:450px;width:122px;height:118px;border-radius:14px 14px 4px 4px;
  background:linear-gradient(90deg,#2a2a2a,#565656 40%,#2a2a2a)}

/* services */
.services{left:0;top:609px;width:717px;height:253px;background:var(--orange)}
.services-title{left:0;top:633px;width:717px;text-align:center;font-weight:700;font-size:15px;color:var(--ink);letter-spacing:.5px}
.services-sub{left:0;top:654px;width:717px;text-align:center;font-size:9px;color:var(--white)}
.service{top:699px;width:150px;text-align:center;color:var(--white)}
.service svg{display:block;margin:0 auto}
.service h4{font-family:"Oswald",Impact,sans-serif;font-weight:700;font-size:13px;color:#111;margin-top:10px;letter-spacing:.2px;white-space:nowrap}
.service p{font-size:6.8px;line-height:10.5px;margin-top:7px}
.service .btn{display:inline-block;margin-top:11px;width:69px;height:16px;line-height:16px;border-radius:9px;
  background:var(--orange-dark);font-size:7px;letter-spacing:.3px}
.services-shadow{left:38px;top:862px;width:640px;height:8px;
  background:radial-gradient(ellipse at 50% 0,rgba(0,0,0,.22),transparent 70%)}

/* lists */
.blog-title{left:62px;top:921px}
.blog-rule{left:193px;top:926px;width:146px}
.post{left:65px;width:272px}
.post h5{font-size:8.5px;color:var(--orange);font-weight:400}
.post p{font-size:6.6px;line-height:9px;margin-top:2px}
.post .more{text-align:right;font-size:6.6px;color:#555;margin-top:8px;padding-bottom:5px;border-bottom:1px solid #e3e3e3}
.post .more::before{content:"";display:inline-block;border-left:5px solid var(--orange);border-top:3px solid transparent;border-bottom:3px solid transparent;margin-right:3px}
.col-title{top:921px}
.link-list li{font-size:6.8px;height:12.8px;line-height:12.8px;color:#555;white-space:nowrap}
.link-list li::before{content:">";color:var(--orange);margin-right:6px}
.link-list.wide li{height:16px;line-height:16px}

/* footer */
.footer-line{left:0;top:1082px;width:717px;height:3px;background:var(--orange)}
.footer{left:0;top:1085px;width:717px;height:115px;background:var(--footer)}
.footer-brand{left:44px;top:1130px;display:flex;align-items:center;gap:5px}
.footer-brand .brand-name{color:var(--white);font-size:10.5px}
.footer-brand .brand-mark{width:13px;height:13px;background:var(--white)}
.copyright{left:68px;top:1165px;font-size:6.2px;color:#aaa}
.foot-list li{height:14px;line-height:13px;font-size:6.5px;color:#ddd;border-bottom:1px dotted var(--footer-line);padding-left:14px;position:relative;white-space:nowrap}
.foot-list li::before{content:"";position:absolute;left:2px;top:4px;border-left:3px solid var(--orange);border-top:2px solid transparent;border-bottom:2px solid transparent}
.foot-list.muted li{color:#aaa}
.contact{left:542px;top:1112px;font-size:6.5px}
.contact div{height:17.6px;display:flex}
.contact dt{color:var(--orange);width:41px}
.contact dd{color:#ddd;font-size:5.8px;white-space:nowrap}
</style>
</head>
<body>

<header>
  <div class="hero abs" role="img" aria-label="Photo of a hand using a laptop touchpad"></div>
  <div class="brand abs"><span class="brand-mark"></span><span class="brand-name">BRIGHTFERN IT SOLUTIONS</span></div>
  <div class="nav-bar abs"></div>
  <nav>
    <a class="nav-link active abs" style="left:390px">HOME</a>
    <a class="nav-link abs" style="left:450px">ABOUT US</a>
    <a class="nav-link abs" style="left:518px">SERVICES</a>
    <a class="nav-link abs" style="left:583px">BLOG</a>
    <a class="nav-link abs" style="left:633px">CONTACT</a>
  </nav>
  <div class="nav-underline abs"></div>
  <ul class="dropdown abs">
    <li>Home &amp; Residential Services</li>
    <li class="on">Customized System build</li>
    <li>Small Business Services</li>
  </ul>
  <div class="hero-text abs">
    <div class="lead">USE OUR SERVICES</div>
    <div class="sub">TO MEET YOUR</div>
    <div class="sub">BUSINESS OBJECTIVES</div>
  </div>
  <div class="dots abs"><span class="on"></span><span></span><span></span></div>
</header>

<section>
  <div class="band abs"></div>
  <p class="band-text abs">For <b>BETTER EXPERIENCE</b> of Online Technical Support <span class="big">24/7</span></p>
  <div class="connect pill abs">CONNECT WITH US</div>
</section>

<section>
  <h2 class="welcome-title section-title abs">WELCOME TO <span class="accent">BRIGHTFERN IT SOLUTIONS</span></h2>
  <div class="welcome-rule rule abs"></div>
  <p class="welcome-copy abs">Contrary to popular belief, Lorem Ipsum is not simply random text. It has roots in a piece of classical Latin literature from 45 BC, making it over 2000 years old. Harold Penwick, a Latin professor at Ashgrove College in Virginia, looked up one of the more obscure Latin words, consectetur, from a Lorem Ipsum passage, and going through the cites of the word in classical literature, discovered the undoubtable source. Lorem Ipsum comes from sections 1.10.32 and 1.10.33 of "de Finibus Bonorum et Malorum" (The Extremes of Good and Evil) by Varenus, written in 45 BC. This book is a treatise on the theory of ethics, very popular during the Renaissance. The first line of Lorem Ipsum, "Lorem ipsum dolor sit amet..", comes from a line in section 1.10.32.</p>
  <div class="read-more pill abs">read more</div>
  <aside class="promo abs">
    <p>AFFORDABLE WEB HOSTING PLANS</p>
    <h3>COMING SOON</h3>
    <small>For the Clients We Love</small>
  </aside>
  <div class="promo-art abs" role="img" aria-label="Illustration of two server towers with blue and orange light strips"></div>
</section>

<section>
  <div class="services abs"></div>
  <h2 class="services-title abs">OUR&nbsp; SERVICES</h2>
  <p class="services-sub abs">Features we are proud lorem ipsum meta data of our company</p>

  <div class="service abs" style="left:37px;top:699px">
    <svg width="54" height="54" viewBox="0 0 54 54" fill="none" stroke="#fff" stroke-width="1.3"><circle cx="27" cy="27" r="26"/><circle cx="27" cy="29" r="7" fill="#fff"/><rect x="22" y="13" width="10" height="7"/><rect x="12" y="26" width="8" height="6"/><rect x="34" y="26" width="8" height="6"/><rect x="22" y="38" width="10" height="5"/></svg>
    <h4>ONSITE SUPPORT</h4>
    <p>Lorem Ipsum is simply dummy text of the printing and typesetting industry. Lorem Ipsum has been the industry.</p>
    <span class="btn">READ MORE</span>
  </div>
  <div class="service abs" style="left:198px;top:699px">
    <svg width="54" height="54" viewBox="0 0 54 54" fill="none" stroke="#fff" stroke-width="1.3"><circle cx="27" cy="27" r="26"/><circle cx="25" cy="25" r="9" stroke-width="4" stroke-dasharray="3 2.5"/><circle cx="25" cy="25" r="3" fill="#fff"/><path d="M30 30l9 9" stroke-width="3"/></svg>
    <h4>TECHNICAL SUPPORT</h4>
    <p>Lorem Ipsum is simply dummy text of the printing and typesetting industry. Lorem Ipsum has been the industry.</p>
    <span class="btn">READ MORE</span>
  </div>
  <div class="service abs" style="left:362px;top:699px">
    <svg width="54" height="54" viewBox="0 0 54 54" fill="none" stroke="#fff" stroke-width="1.3"><circle cx="27" cy="27" r="26"/><path d="M20 25a7 7 0 1 1 14 0c0 4-4 6-4 9h-6c0-3-4-5-4-9z" stroke-width="1.8"/><path d="M24 38h6M25 41h4"/><path d="M28 20l-3 5h4l-3 5" /></svg>
    <h4>NETWORK SOLUTIONS</h4>
    <p>Lorem Ipsum is simply dummy text of the printing and typesetting industry. Lorem Ipsum has been the industry.</p>
    <span class="btn">READ MORE</span>
  </div>
  <div class="service abs" style="left:527px;top:699px">
    <svg width="54" height="54" viewBox="0 0 54 54" fill="none" stroke="#fff" stroke-width="1.3"><circle cx="27" cy="27" r="26"/><path d="M16 34l10-10 6 6-10 10z" fill="#fff"/><rect x="14" y="36" width="20" height="4" fill="#fff"/><path d="M30 20a8 8 0 0 1 8 8M30 15a13 13 0 0 1 13 13" stroke-width="2"/></svg>
    <h4>REMOTE SUPPORT</h4>
    <p>Lorem Ipsum is simply dummy text of the printing and typesetting industry. Lorem Ipsum has been the industry.</p>
    <span class="btn">READ MORE</span>
  </div>
  <div class="services-shadow abs"></div>
</section>

<section>
  <h2 class="blog-title section-title abs">LATEST BLOG POSTS</h2>
  <div class="blog-rule rule abs"></div>
  <article class="post abs" style="top:952px">
    <h5>Aenean tincidunt eros at luctus</h5>
    <p>Integer facilisis pharetra risus eget auctor. Nullam viverra dapibus tellus, sit amet cursus turpis vulputate consectetur.</p>
    <div class="more">Read More</div>
  </article>
  <article class="post abs" style="top:1002px">
    <h5>Aenean tincidunt eros at luctus</h5>
    <p>Integer facilisis pharetra risus eget auctor. Nullam viverra dapibus tellus, sit amet cursus turpis vulputate consectetur.</p>
    <div class="more">Read More</div>
  </article>

  <h2 class="col-title section-title abs" style="left:378px">POPULAR</h2>
  <ul class="link-list abs" style="left:378px;top:956px">
    <li>PC System Setup</li><li>Re-installation of Operating System</li><li>Virus Removal</li>
    <li>Data backup and Restore</li><li>Customized System build</li><li>Home and Wireless Networking</li>
    <li>FibreLink Smart Wiring service</li>
  </ul>

  <h2 class="col-title section-title abs" style="left:531px">FEATURED</h2>
  <ul class="link-list wide abs" style="left:531px;top:954px">
    <li>Small Business Services</li><li>Email Hosting</li><li>Domain hosting</li><li>At Hourly Rate</li><li>Coming Soon</li>
  </ul>
</section>

<footer>
  <div class="footer-line abs"></div>
  <div class="footer abs"></div>
  <div class="footer-brand abs"><span class="brand-mark"></span><span class="brand-name">BRIGHTFERN IT SOLUTIONS</span></div>
  <p class="copyright abs">© 2015 All rights reserved.</p>
  <ul class="foot-list abs" style="left:220px;top:1107px;width:102px">
    <li>Home</li><li>About Us</li><li>Services</li><li>Blog</li><li>Contact Us</li>
  </ul>
  <ul class="foot-list muted abs" style="left:386px;top:1106px;width:122px">
    <li>Home &amp; Residential Services</li><li>PC System Setup $ 88/HR</li><li>Virus Removal $105</li><li>Small Business Services</li><li>More</li>
  </ul>
  <dl class="contact abs">
    <div><dt>Address:</dt><dd>PO BOX TBA</dd></div>
    <div><dt>Phone:</dt><dd>0864015738</dd></div>
    <div><dt>E-mail:</dt><dd>INQUIRIES@BRIGHTFERNIT.NET.AU</dd></div>
    <div><dt>Website:</dt><dd>www.brightfernit.net.au</dd></div>
  </dl>
</footer>

</body>
</html>
```